Information Management & Advanced Analytics Company Needs a Web Design

We need a web design for a new company based in Singapore called Korvelt Solutions. We provides information management and advanced analytics services and solutions across a wide variety of industries (Financial Services, Government and Public Sector, Oil & Gas among others). We are not like any other System Integrator, as we believe in bringing together the science and art of data (and data science) to our clients. Science in the sense of understanding technology and Art in the sense of how to operationalise across a culture/people/processes. As with the name of the company Korvelt, which is a play on the words 'Ascending', we want a final design should communicate growth and our ability to help an organisation ascend towards better outcomes.

We have put some very high level ideas in a document however happy to leave an open hand for ideas and recommendation on design. Content can be incorporated/updated moving forwards.

To clarify on the scope of the work (thanks for the feedback); it is to create a framework for 5 pages (1 is comprehensive - services, while 2 are purely information to public, such as about us and contact us and finally join us and partners may have some dynamic information that will be updated). We would like to create a simple, yet elegant site that is intuitive and communicates progression and growth. We are open to ideas on design hence trying to first focus on look/feel/flow and then fill up with detailed content. Thanks.

Note that 'Join Us' is for hiring purposes (open positions and submission of CVs).

1. Possible to request for a more Asian look.
2. You may want to take a look at this site, www.plendrix.com, website designs are moving towards this manner to support different devices and platforms.
Updates

Hi all,1. Possible to request for a more Asian look especially the stock pictures that are used.2. Take a look at this site, www.plendrix.com, website designs are moving towards this manner to support different devices and platforms. More use of infographics too. Added Tuesday, October 6, 2015

Project Deadline Extended Reason: We would like a more Asian look given our operating location. Likewise, we would like designers to consider a design that will support different devices and platforms such as www.plendrix.com. As such we would like to provide more time. Thanks. Added Tuesday, October 6, 2015

Target Market(s)

We provide implementation and consultancy services to a wide range of industries. The audience/market would be those seeking for; 1. Revenue Enhancement, 2. Operations Optimisation, 3. Risk Management

Industry/Entity Type

Information Technology

Coding

Coded - Design and coding required

Number of Pages Required

5+ page

Font styles to use
Sans Serif

Requirements
Must have
• Other than the landing page we should have the following pages (in no particular order); Services, About Us, Contact Us, Join Us, Partners.
• Our main service areas and focus are
• - Information Management
• - Advanced Analytics
Nice to have
• Given our approach of art and science, it would be nice to have a design that captures that essence of combining technology with consultancy.
• Regarding colors, see the uploaded company logo for ideas of color schemes to use and align to.
Should not have
• The site should be accessible from handheld devices so drop down menus are not advisable as they do not always function on these devices.

```html
<!DOCTYPE html>
<html lang="en">
<head>
<meta charset="utf-8">
<title>Korvelt Solutions</title>
<link rel="stylesheet" href="https://fonts.googleapis.com/css2?family=Open+Sans:wght@300;400;600;700&display=swap">
<style>
:root{
  --orange:#f2622e;
  --orange-dark:#d94f1f;
  --charcoal:#2b2b2b;
  --slate:#3c3c3c;
  --grey:#6b6b6b;
  --light:#f4f4f4;
  --white:#ffffff;
  --line:#dddddd;
}
*{box-sizing:border-box;margin:0;padding:0}
html,body{width:1200px;height:2332px;overflow:hidden}
body{font-family:"Open Sans",Arial,sans-serif;color:var(--charcoal);background:var(--white);position:relative}

.site-header{position:absolute;top:0;left:0;width:1200px;height:60px;background:rgba(40,40,40,.82);z-index:5}
.nav-link{position:absolute;top:0;height:60px;line-height:60px;color:var(--white);font-size:17px;text-align:center}
.nav-link.active{background:var(--orange)}
.brand{position:absolute;left:480px;top:0;width:240px;height:60px;display:flex;align-items:center;justify-content:center;gap:10px}
.brand-mark{width:16px;height:16px;background:var(--orange)}
.brand-name{font-size:26px;font-weight:400;color:var(--white);line-height:60px}

.hero{position:absolute;top:0;left:0;width:1200px;height:672px;background:linear-gradient(120deg,#5a5a5a 0%,#8a8a8a 35%,#b8b8b8 60%,#9a9a9a 100%)}
.hero-photo{position:absolute;inset:0;background:radial-gradient(ellipse at 28% 55%,#6c7380 0%,rgba(60,60,60,0) 45%),radial-gradient(ellipse at 70% 80%,rgba(200,180,160,.5) 0%,rgba(0,0,0,0) 50%)}
.hero-arrow{position:absolute;top:306px;color:var(--white);font-size:30px}
.hero-panel{position:absolute;left:632px;top:244px;width:488px;height:336px;background:rgba(255,255,255,.82);text-align:center;padding-top:24px}
.hero-title{font-size:52px;font-weight:300;color:var(--orange)}
.hero-text{font-size:24px;color:var(--grey);line-height:32px;margin:10px auto 0;width:360px}
.btn{display:inline-block;background:var(--orange);color:var(--white);text-align:center}
.hero-btn{margin-top:26px;width:280px;height:72px;line-height:72px;font-size:28px}

.offer{position:absolute;top:672px;left:0;width:1200px;height:488px;background:var(--white);text-align:center}
.section-title{font-size:44px;font-weight:300;color:var(--orange)}
.offer .section-title{margin-top:44px}
.section-sub{font-size:17px;color:var(--grey);margin-top:6px}
.cards{position:absolute;top:176px;left:212px;display:flex}
.card{width:258px;height:256px;border:1px solid var(--line);padding-top:36px}
.card.featured{background:var(--orange);border-color:var(--orange)}
.card h3{font-size:17px;font-weight:400;color:var(--orange);margin-top:14px}
.card p{font-size:15px;color:var(--grey);width:160px;margin:6px auto 0;line-height:20px}
.card.featured h3,.card.featured p{color:var(--white)}

.about{position:absolute;top:1160px;left:0;width:1200px;height:320px;background:linear-gradient(90deg,#3a3a3a,#555 50%,#3c3c3c);text-align:center}
.about .section-title{margin-top:14px;color:var(--orange)}
.about-text{color:#eeeeee;font-size:17px;line-height:26px;width:660px;margin:14px auto 0}
.outline-btn{display:inline-block;margin-top:22px;border:1px solid var(--white);color:var(--white);width:160px;height:52px;line-height:50px;font-size:17px}

.partners{position:absolute;top:1480px;left:0;width:1200px;height:410px;background:linear-gradient(180deg,rgba(240,120,70,.85),rgba(235,95,45,.95)),linear-gradient(90deg,#c96,#eba);text-align:center}
.partners .section-title{margin-top:36px;color:var(--white)}
.partners .section-sub{color:var(--white)}
.badges{display:flex;justify-content:center;gap:14px;margin-top:66px}
.badge{width:168px;height:96px;background:var(--white);display:flex;align-items:center;justify-content:center}
.badge span{display:block;width:104px;height:40px;background:#e3e3e3;border-radius:4px}

.newsletter{position:absolute;top:1890px;left:0;width:1200px;height:110px;background:var(--slate)}
.newsletter h2{position:absolute;left:362px;top:24px;font-size:40px;font-weight:300;color:var(--orange)}
.field{position:absolute;left:596px;top:30px;width:270px;height:48px;background:var(--white);border:1px solid #ccc;color:var(--grey);font-size:15px;padding:12px}
.submit-btn{position:absolute;left:876px;top:30px;width:156px;height:48px;line-height:48px;font-size:20px}

.contact{position:absolute;top:2000px;left:0;width:1200px;height:264px}
.map{position:absolute;inset:0;background:linear-gradient(135deg,#e9e5dc 0%,#d9e4cf 40%,#bfd6e6 75%,#a9cbe3 100%)}
.touch{position:absolute;left:120px;top:16px;width:320px;height:248px;background:var(--orange);color:var(--white);padding:18px 22px}
.touch h3{font-size:22px;font-weight:400;margin-bottom:14px}
.touch-row{display:flex;gap:14px;font-size:13px;line-height:18px;margin-bottom:16px;text-transform:uppercase}
.touch-row svg{flex:none}

.site-footer{position:absolute;top:2264px;left:0;width:1200px;height:68px;background:var(--charcoal)}
.copyright{position:absolute;left:30px;top:24px;font-size:14px;color:#bbbbbb}
.copyright b{color:var(--orange);font-weight:400}
.social{position:absolute;right:36px;top:20px;display:flex;gap:22px}
.social span{width:26px;height:26px;border-radius:50%;background:var(--orange)}
</style>
</head>
<body>

<section class="hero">
  <div class="hero-photo" role="img" aria-label="Smiling businessman offering a handshake in front of a cheering team"></div>
  <span class="hero-arrow" style="left:26px">&#8249;</span>
  <span class="hero-arrow" style="right:26px">&#8250;</span>
  <div class="hero-panel">
    <h1 class="hero-title">If You Like Us</h1>
    <p class="hero-text">We will have a paragraph to talk about who we are</p>
    <span class="btn hero-btn">Join Us</span>
  </div>
</section>

<header class="site-header">
  <span class="nav-link active" style="left:64px;width:112px">Home</span>
  <span class="nav-link" style="left:186px;width:108px">About Us</span>
  <span class="nav-link" style="left:304px;width:100px">Services</span>
  <div class="brand">
    <span class="brand-mark"></span>
    <span class="brand-name">Korvelt</span>
  </div>
  <span class="nav-link" style="left:780px;width:130px">Our Partners</span>
  <span class="nav-link" style="left:920px;width:90px">Join us</span>
  <span class="nav-link" style="left:1020px;width:112px">Contact us</span>
</header>

<section class="offer">
  <h2 class="section-title">What We Offer</h2>
  <p class="section-sub">our service areas and focus.</p>
  <div class="cards">
    <div class="card">
      <svg width="56" height="56" viewBox="0 0 56 56" fill="none" stroke="#555" stroke-width="3"><circle cx="22" cy="22" r="10"/><circle cx="22" cy="22" r="3"/><circle cx="40" cy="38" r="7"/><path d="M22 6v6M22 32v6M6 22h6M32 22h6"/></svg>
      <h3>Information &amp; Management</h3>
      <p>Lorem Ipsum is simply dummy text of the</p>
    </div>
    <div class="card featured">
      <svg width="56" height="56" viewBox="0 0 56 56" fill="none" stroke="#fff" stroke-width="3"><path d="M8 48h40"/><rect x="12" y="30" width="7" height="16"/><rect x="25" y="20" width="7" height="26"/><rect x="38" y="10" width="7" height="36"/></svg>
      <h3>Advanced Analytics</h3>
      <p>Lorem Ipsum is simply dummy text of the</p>
    </div>
    <div class="card">
      <svg width="56" height="56" viewBox="0 0 56 56" fill="none" stroke="#555" stroke-width="3"><rect x="10" y="8" width="30" height="38" rx="3"/><circle cx="38" cy="38" r="10"/><path d="M33 38l4 4 7-8"/></svg>
      <h3>Risk Management</h3>
      <p>Lorem Ipsum is simply dummy text of the</p>
    </div>
  </div>
</section>

<section class="about" role="img" aria-label="Group of smiling professionals behind a dark overlay">
  <h2 class="section-title">Who We Are</h2>
  <p class="about-text">What is Korvelt, what do we stand for and what brought us together to deliver to the marketplace. This page will also rely on the four founders of the company i.e. a photo and a short brief of each founder</p>
  <span class="outline-btn">Read More</span>
</section>

<section class="partners" role="img" aria-label="Team of professionals under an orange overlay">
  <h2 class="section-title">Our Partners</h2>
  <p class="section-sub">some information about the partners we work with and can work on</p>
  <div class="badges">
    <div class="badge"><span></span></div>
    <div class="badge"><span></span></div>
    <div class="badge"><span></span></div>
    <div class="badge"><span></span></div>
    <div class="badge"><span></span></div>
    <div class="badge"><span></span></div>
  </div>
</section>

<section class="newsletter">
  <h2>Newsletter</h2>
  <div class="field">Email Id</div>
  <span class="btn submit-btn">Submit</span>
</section>

<section class="contact">
  <div class="map" role="img" aria-label="Street map of Singapore with office location pin"></div>
  <div class="touch">
    <h3>Keep In Touch</h3>
    <div class="touch-row">
      <svg width="20" height="26" viewBox="0 0 20 26"><path d="M10 0C4.5 0 0 4.5 0 10c0 7 10 16 10 16s10-9 10-16C20 4.5 15.5 0 10 0z" fill="#fff"/><circle cx="10" cy="10" r="4" fill="#f2622e"/></svg>
      <div>12, Harbour View Road<br>#07-03<br>Meridian Centre<br>Singapore 000000</div>
    </div>
    <div class="touch-row">
      <svg width="20" height="20" viewBox="0 0 20 20"><path d="M4 1l4 4-2 3c1 3 3 5 6 6l3-2 4 4-3 3C8 19 1 12 1 4z" fill="#fff"/></svg>
      <div>+1234567890</div>
    </div>
  </div>
</section>

<footer class="site-footer">
  <p class="copyright"><b>&copy; Korvelt Solutions</b> - 2015. All Rights Reserved</p>
  <div class="social"><span></span><span></span><span></span></div>
</footer>

</body>
</html>
```